Wesbite design for Investment Firm

We want a basic (clean) website that follows the form, fonts and colors of our attachments. This is for a financial investment management firm, but we have a boutique (anti-Wall Street) approach. Site should have an Home Page (Logo up top - room for basic copy on bottom, Philosophy Page (room for Quarterly Letter attachment and basic copy, Performance Page (room for Performance Overview and Performance Analysis and basic copy), Team Page, Commentary Page and Contact
Updates

Reason: Some designers have asked for an extension. Again, please only use image of Train Station or Train Station Logo in design.

Target Market(s)

Small and mid-size financial advisors from across the country

Industry/Entity Type

Financial

Number of Pages Required

5+ page

Font styles to use
Other font styles liked:
• Palotino Linotype

Colors
3176b5
cfdeed
ffffff

Requirements
Must have
• Please refer to existing site www.qarvelton.com. Of note, this is too complex / cluttered. We simply want Blur, Grey and White consistent with attachments. The copy is pretty good, but will be simplified (and no quotes)
Should not have
• No images other than train station logo and / or train station image

```html
<!DOCTYPE html>
<html lang="en">
<head>
<meta charset="utf-8">
<title>Qarvelton Investment Company</title>
<link rel="stylesheet" href="https://fonts.googleapis.com/css2?family=EB+Garamond:wght@400;500&family=Open+Sans:wght@400;600;700&display=swap">
<style>
:root{
  --blue:#3176b5;
  --blue-deep:#1f4f8f;
  --pale:#cfdeed;
  --grey:#eeeef0;
  --white:#ffffff;
  --ink:#333a44;
  --muted:#5a606a;
}
*{box-sizing:border-box;margin:0;padding:0}
html,body{width:1200px;height:2299px;overflow:hidden}
body{position:relative;background:var(--white);font-family:"Open Sans",Arial,sans-serif;color:var(--ink)}
.abs{position:absolute}

/* Hero */
.hero{left:0;top:0;width:1200px;height:678px;background:linear-gradient(180deg,#3a69a8 0%,#7c9cc4 30%,#c89a7a 45%,#6b5a52 60%,#4a4548 100%)}
.brand{left:130px;top:22px;color:var(--white);font-family:"EB Garamond",Georgia,serif}
.brand-name{font-size:34px;font-weight:400;letter-spacing:.2px;line-height:1}
.brand-tag{font-size:14px;margin-top:6px;padding-left:116px}
.nav{left:585px;top:22px;display:flex;gap:0;list-style:none}
.nav li{font-size:12px;font-weight:700;color:var(--white);padding:4px 11px}
.nav li.active{border:2px solid var(--white);padding:2px 9px}
.hero-caption{left:100px;top:472px;width:406px;height:180px;border:1px solid rgba(255,255,255,.7);background:rgba(255,255,255,.12);padding:32px 0 0 34px;color:var(--white)}
.hero-caption h1{font-size:34px;font-weight:700;line-height:1.15}
.hero-caption p{font-size:33px;font-weight:400;line-height:1.1}
.btn-white{left:138px;top:605px;width:147px;height:35px;background:var(--white);color:var(--blue-deep);font-size:14px;font-weight:700;display:flex;align-items:center;justify-content:center}
.dots{display:flex;gap:16px}
.dot{width:11px;height:11px;border-radius:50%;background:var(--white)}
.dot.on{background:#3fc7a6}
.hero-dots{left:598px;top:610px}

/* Welcome */
.welcome{left:132px;top:748px;width:440px;height:314px;border:2px solid #d6d8dc;padding:48px 46px 0 45px}
.welcome small{font-size:14px;color:var(--ink);display:block}
.welcome h2{font-size:22px;font-weight:400;color:var(--blue-deep);margin:6px 0 22px}
.welcome p{font-size:11.4px;line-height:20px;color:var(--muted)}
.btn-blue{background:var(--blue);color:var(--white);font-size:11px;font-weight:700;display:flex;align-items:center;justify-content:center}
.welcome .btn-blue{width:102px;height:31px;margin-top:20px}
.photo{left:572px;top:730px;width:496px;height:352px;background:linear-gradient(160deg,#6c7077 0%,#d9dde2 35%,#f3f4f5 55%,#8f969d 100%);box-shadow:0 6px 18px rgba(0,0,0,.22)}

/* Features */
.features{left:0;top:1200px;width:1200px;height:310px;background:var(--grey)}
.feature{top:1153px;width:340px;text-align:center}
.feature .ring{width:128px;height:128px;border-radius:50%;background:var(--grey);border:7px solid var(--white);margin:0 auto;display:flex;align-items:center;justify-content:center}
.feature h3{font-size:15px;font-weight:600;color:var(--blue-deep);margin-top:37px}
.feature p{font-size:11.2px;line-height:18px;color:var(--ink);margin:17px auto 0;width:240px}
.feature .btn-blue{width:88px;height:25px;margin:22px auto 0}
.divider-v{top:1307px;width:1px;height:164px;background:#d4d6da}

/* Quote */
.quote{left:0;top:1510px;width:1200px;height:357px;background:linear-gradient(180deg,#dbe5f0 0%,var(--pale) 100%)}
.quote-text{left:370px;top:1602px;width:460px;text-align:center;font-size:15px;line-height:24px;color:var(--ink)}
.quote-mark{font-family:Georgia,serif;font-size:64px;font-weight:700;color:var(--blue);line-height:1}
.quote-rule{left:518px;top:1740px;width:164px;height:2px;background:var(--blue-deep)}
.quote-by{left:400px;top:1758px;width:400px;text-align:center;font-size:11.5px;color:var(--muted)}
.quote-dots{left:567px;top:1815px;gap:10px}
.quote-dots .dot{width:6px;height:6px;background:#eef3f9}
.quote-dots .dot.on{background:var(--blue)}

/* Footer */
.footer{left:0;top:1867px;width:1200px;height:432px;background:var(--blue);color:var(--white)}
.f-col{top:1916px}
.f-col h4{font-size:14px;font-weight:700;line-height:18px;text-transform:uppercase}
.letter-thumb{left:132px;top:1967px;width:141px;height:179px;background:var(--white);border:2px solid #dfe6ee}
.contact-list{list-style:none;margin-top:30px;font-size:11.5px;line-height:18px}
.contact-list li{display:flex;gap:16px;margin-bottom:28px}
.contact-list svg{flex:none;margin-top:3px}
.menu-list{list-style:none;margin-top:26px;font-size:11.5px}
.menu-list li{margin-bottom:15px}
.post-date{font-size:9px;margin-top:28px;letter-spacing:.3px}
.post-title{font-size:11px;font-weight:700;margin-top:4px}
.post-text{font-size:11.2px;line-height:18px;margin-top:14px;width:240px}
.btn-pale{width:78px;height:27px;background:var(--pale);color:var(--blue);font-size:10.5px;font-weight:700;display:flex;align-items:center;justify-content:center;margin-top:22px}
.footer-rule{left:132px;top:2203px;width:934px;height:1px;background:rgba(255,255,255,.35)}
.copyright{left:0;top:2244px;width:1200px;text-align:center;font-size:11.5px}
</style>
</head>
<body>

<section class="abs hero" role="img" aria-label="Aerial photograph of a downtown city skyline at sunset"></section>
<div class="abs brand">
  <div class="brand-name">Qarvelton Investment Company</div>
  <div class="brand-tag">Separately Managed Accounts</div>
</div>
<ul class="abs nav">
  <li class="active">Home</li><li>Philosophy</li><li>Performance</li><li>Team</li><li>Letters</li><li>Commentary</li><li>Contact</li>
</ul>
<div class="abs hero-caption">
  <h1>Financial Investment</h1>
  <p>Management Firm</p>
</div>
<div class="abs btn-white">READ MORE</div>
<div class="abs dots hero-dots"><span class="dot"></span><span class="dot"></span><span class="dot on"></span><span class="dot"></span><span class="dot"></span></div>

<section class="abs welcome">
  <small>WELCOME TO</small>
  <h2>Qarvelton Investment Company</h2>
  <p>We founded Qarvelton Investment Company in 1999, initially managing wealth from our family and friends in the town of Qarvelton. The high expectations of our original investors is a key contributor to our value driven investment philosophy.</p>
  <div class="btn-blue">READ MORE</div>
</section>
<div class="abs photo" role="img" aria-label="Photograph of the white clapboard train station building"></div>

<section class="abs features"></section>
<div class="abs feature" style="left:75px">
  <div class="ring"><svg width="56" height="56" viewBox="0 0 56 56"><circle cx="28" cy="28" r="26" fill="none" stroke="#3176b5" stroke-width="3"/><path d="M28 2a13 13 0 0 1 0 26a13 13 0 0 0 0 26a26 26 0 0 1 0-52z" fill="#3176b5"/><circle cx="28" cy="15" r="4" fill="#3176b5"/><circle cx="28" cy="41" r="4" fill="#fff"/></svg></div>
  <h3>Philosophy</h3>
  <p>Our proprietary investment research seeks to determine the appraised value of a company.</p>
  <div class="btn-blue">READ MORE</div>
</div>
<div class="abs divider-v" style="left:411px"></div>
<div class="abs feature" style="left:413px">
  <div class="ring"><svg width="56" height="52" viewBox="0 0 56 52"><rect x="4" y="30" width="7" height="18" fill="#3176b5"/><rect x="15" y="24" width="7" height="24" fill="#3176b5"/><rect x="26" y="28" width="7" height="20" fill="#3176b5"/><rect x="37" y="18" width="7" height="30" fill="#3176b5"/><polyline points="6,22 18,14 29,20 46,6" fill="none" stroke="#3176b5" stroke-width="3"/><polygon points="40,4 50,2 48,12" fill="#3176b5"/></svg></div>
  <h3>Performance</h3>
  <p>We believe trying to keep pace with the market in all environments promotes poor decisions</p>
  <div class="btn-blue">READ MORE</div>
</div>
<div class="abs divider-v" style="left:756px"></div>
<div class="abs feature" style="left:753px">
  <div class="ring"><svg width="60" height="44" viewBox="0 0 60 44" fill="#3176b5"><circle cx="30" cy="8" r="6"/><circle cx="18" cy="16" r="5"/><circle cx="42" cy="16" r="5"/><circle cx="8" cy="24" r="4.5"/><circle cx="52" cy="24" r="4.5"/><path d="M22 30a8 8 0 0 1 16 0v10H22z"/><path d="M11 34a7 7 0 0 1 14 0v6H11zM35 34a7 7 0 0 1 14 0v6H35z"/><path d="M1 38a7 7 0 0 1 14 0v4H1zM45 38a7 7 0 0 1 14 0v4H45z"/></svg></div>
  <h3>Team</h3>
  <p>Daniel is the cofounder and Managing Member of Qarvelton and serves as portfolio manager for the firm's Core Equity strategy.</p>
  <div class="btn-blue">READ MORE</div>
</div>

<section class="abs quote" role="img" aria-label="Faint city skyline photograph behind the quotation"></section>
<div class="abs quote-mark" style="left:345px;top:1556px">&ldquo;</div>
<p class="abs quote-text">An investment operation is one which, upon thorough analysis, promises safety of principal and an adequate return. Operations not meeting these requirements are speculative</p>
<div class="abs quote-mark" style="left:780px;top:1666px">&rdquo;</div>
<div class="abs quote-rule"></div>
<p class="abs quote-by">- Harlan Whitcomb, The Patient Holder</p>
<div class="abs dots quote-dots"><span class="dot"></span><span class="dot"></span><span class="dot on"></span><span class="dot"></span></div>

<footer class="abs footer"></footer>
<div class="abs f-col" style="left:132px"><h4>Investment<br>Adviser's Letter</h4></div>
<div class="abs letter-thumb" role="img" aria-label="Cover of the investment adviser's letter with a sketch of the train station"></div>
<div class="abs f-col" style="left:357px;color:#fff">
  <h4>Contact Us</h4>
  <ul class="contact-list">
    <li><svg width="9" height="12" viewBox="0 0 9 12"><path d="M4.5 0A4.5 4.5 0 0 0 0 4.5C0 8 4.5 12 4.5 12S9 8 9 4.5A4.5 4.5 0 0 0 4.5 0z" fill="#fff"/><circle cx="4.5" cy="4.5" r="1.6" fill="#3176b5"/></svg><span>2710 Maple Crest Avenue,<br>Suite 820<br>Dallas, TX 75201</span></li>
    <li><svg width="11" height="11" viewBox="0 0 11 11"><path d="M2 0l2 3-1.2 1.3a7 7 0 0 0 3.9 3.9L8 7l3 2-1 2C4.5 11 0 6.5 0 1z" fill="#fff"/></svg><span>214.555.0186</span></li>
    <li><svg width="11" height="9" viewBox="0 0 11 9"><rect width="11" height="9" rx="1" fill="#fff"/><path d="M0 1l5.5 4L11 1" fill="none" stroke="#3176b5" stroke-width="1.2"/></svg><span>info@qarvelton.com</span></li>
  </ul>
</div>
<div class="abs f-col" style="left:599px">
  <h4>Menu</h4>
  <ul class="menu-list">
    <li>Performance Overview</li><li>Performance Analysis</li><li>Verification Statement</li><li>Qarvelton ADV Part 2</li>
  </ul>
</div>
<div class="abs f-col" style="left:829px">
  <h4>Latest Commentary</h4>
  <p class="post-date">AUGUST 10, 2017</p>
  <p class="post-title">CORE EQUITY PORTFOLIO – Q2 2017</p>
  <p class="post-text">Based on our estimate of fair value relative to the company's current stock price, we determine each company's current margin of safety in the Core Equity</p>
  <div class="btn-pale">READ MORE</div>
</div>
<div class="abs footer-rule"></div>
<p class="abs copyright" style="color:#fff">Copyrights @ 2017 All Rights Reserved</p>

</body>
</html>
```